New website design for small car detailing company.

We have a small cleaning company, our main focus is car detailing but we are also expanding to home and residential cleaning and power washing.
I would like the web site to have a simple layout and SEO friendly.
I would also like to have a contact page in which clients can contact us and upload pictures of the house or car so we can provide an estimate.
A Page that shows the services we offer.

Target Market(s)

High paying clients for car detailiing and focus on residential and commercial cleaning.

Industry/Entity Type

Cleaning Service

Coding

Coded - Design and coding required

Number of Pages Required

4 page

Font styles to use
Serif

Colors

Designer to choose only greyscale colors for use in the design.

Requirements
Must have
• A home page.
Blog page for SEO
Contact page with the choice of clients to upload theirs pictures so we can provide estimates with calendar integration so they can provide their available dates for service.
A pictures to sell our services.
Nice to have
• Simple but sleek desing, I am more interested in SEO Score than heavy loads

```html
<!DOCTYPE html>
<html lang="en">
<head>
<meta charset="utf-8">
<title>Harbor Line Mobile Detailing</title>
<link href="https://fonts.googleapis.com/css2?family=Montserrat:wght@400;500;600;700&family=Open+Sans:wght@400;600&display=swap" rel="stylesheet">
<style>
:root{
  --ink:#1b1b1b;
  --text:#3a3a3a;
  --muted:#7a7a7a;
  --line:#d4d4d4;
  --paper:#ffffff;
  --soft:#f3f3f3;
  --dark:#161616;
  --band:#4a4a4a;
  --accent:#c9bb9c;
}
*{margin:0;padding:0;box-sizing:border-box}
html,body{width:1200px;height:5084px;overflow:hidden;background:var(--paper)}
body{font-family:"Open Sans",Arial,sans-serif;color:var(--text);position:relative}
h1,h2,h3,h4,.nav,.btn,.eyebrow{font-family:"Montserrat",Arial,sans-serif}
.abs{position:absolute}
section,header,footer{position:absolute;left:0;width:1200px}
.btn{display:inline-block;background:var(--ink);color:#fff;font-size:13px;font-weight:600;padding:9px 22px;border-radius:18px}
.eyebrow{font-size:15px;letter-spacing:1px;color:var(--muted);font-weight:500}
.section-title{text-align:center}
.section-title .eyebrow{display:block;margin-bottom:10px}
.section-title h2{font-size:26px;font-weight:700;color:var(--ink);letter-spacing:.5px}
.photo{position:absolute}

/* header */
.site-header{top:0;height:64px;z-index:5}
.brand-tab{position:absolute;left:88px;top:0;width:92px;height:118px;background:var(--ink);color:#fff;font-family:"Montserrat",sans-serif;font-weight:600;font-size:12px;text-align:center;padding-top:42px;line-height:1.5;letter-spacing:.5px}
.nav{position:absolute;right:100px;top:22px;display:flex;gap:30px;align-items:center;font-size:13px;font-weight:600;color:var(--ink)}
.nav .current{color:var(--muted)}
.nav .pill{background:var(--ink);color:#fff;padding:6px 16px;border-radius:16px}

/* hero */
.hero{top:0;height:780px;overflow:hidden}
.hero .photo{left:0;top:0;width:1200px;height:760px;background:linear-gradient(180deg,#e8e8e8 0%,#bdbdbd 25%,#6e6e6e 60%,#3d3d3d 100%)}
.hero-copy{position:absolute;top:300px;width:1200px;text-align:center;color:#fff}
.hero-copy .l1{font-family:"Montserrat",sans-serif;font-size:40px;font-weight:500;letter-spacing:2px}
.hero-copy .l2{font-family:"Montserrat",sans-serif;font-size:42px;font-weight:700;letter-spacing:1px;margin-top:4px}
.hero-copy .btn{margin-top:30px;background:#fff;color:var(--ink);border:2px solid var(--ink);border-radius:4px;padding:8px 26px}
.hero-arrow{position:absolute;top:330px}
.dots{position:absolute;display:flex;gap:10px}
.dots i{width:10px;height:10px;border-radius:50%;background:#cfcfcf;display:block}
.dots i.on{background:#fff}

/* about */
.about{top:780px;height:420px}
.about .eyebrow{position:absolute;left:128px;top:50px}
.about h2{position:absolute;left:128px;top:80px;font-size:25px;font-weight:700;color:var(--ink);line-height:1.3}
.about p{position:absolute;left:128px;top:160px;width:430px;font-size:13px;line-height:1.55}
.about .btn{position:absolute;left:128px;top:288px;border-radius:6px}
.about .photo{left:605px;top:40px;width:515px;height:330px;background:linear-gradient(135deg,#3a3a3a,#777 55%,#2b2b2b)}
.about .frame{position:absolute;left:625px;top:20px;width:510px;height:330px;border:2px solid var(--line)}

/* services */
.services{top:1200px;height:572px}
.services .section-title{position:absolute;top:28px;width:1200px}
.service{position:absolute;top:140px;width:210px}
.service .icon{width:96px;height:96px;border-radius:50%;border:2px solid #333;display:flex;align-items:center;justify-content:center}
.service .icon.active{background:#9a9a9a;border-color:#9a9a9a}
.service h3{font-size:15px;font-weight:700;color:var(--ink);margin-top:40px;line-height:1.3;min-height:40px}
.service p{font-size:13px;line-height:1.5;margin-top:8px}
.services .btn{position:absolute;left:380px;top:485px;border-radius:6px}

/* why */
.why{top:1772px;height:536px;background:var(--soft)}
.why .photo{left:130px;top:20px;width:480px;height:516px;background:radial-gradient(ellipse at 50% 55%,#cfcfcf 0%,#e8e8e8 55%,var(--soft) 80%)}
.why .eyebrow{position:absolute;left:668px;top:72px}
.why h2{position:absolute;left:668px;top:100px;font-size:27px;font-weight:700;color:var(--ink);line-height:1.25}
.why p{position:absolute;left:668px;top:200px;width:400px;font-size:13px;line-height:1.55}
.why ul{position:absolute;left:668px;top:282px;list-style:none;font-family:"Montserrat",sans-serif;font-size:13px;font-weight:500;color:var(--ink)}
.why li{margin-bottom:22px;display:flex;align-items:center;gap:16px}
.why .btn{position:absolute;left:668px;top:452px;border-radius:6px}

/* stats */
.stats{top:2308px;height:340px}
.stats svg.band{position:absolute;left:0;top:0}
.stat{position:absolute;top:80px;width:150px;text-align:center;color:#fff}
.stat .ring{width:92px;height:92px;border-radius:50%;border:3px solid #fff;margin:0 auto;display:flex;align-items:center;justify-content:center;font-family:"Montserrat",sans-serif;font-size:26px;font-weight:600}
.stat span{display:block;font-size:15px;margin-top:14px;line-height:1.3}

/* testimonials */
.testimonials{top:2660px;height:480px}
.testimonials .section-title{position:absolute;top:24px;width:1200px}
.testimonials .rail{position:absolute;left:465px;top:190px;width:270px;height:2px;background:var(--line)}
.testimonials .avatar{position:absolute;left:553px;top:140px;width:94px;height:94px;border-radius:50%;background:linear-gradient(160deg,#8a8a8a,#3a3a3a);border:4px solid #fff}
.testimonials .arrow{position:absolute;top:170px;width:42px;height:42px;border:2px solid #333;border-radius:50%;display:flex;align-items:center;justify-content:center;background:#fff}
.testimonials blockquote{position:absolute;left:170px;top:300px;width:860px;text-align:center;font-size:13px;line-height:1.6}
.testimonials cite{position:absolute;top:375px;width:1200px;text-align:center;font-style:normal;font-family:"Montserrat",sans-serif;font-size:12px;letter-spacing:1px}
.testimonials .stars{position:absolute;top:398px;width:1200px;text-align:center;font-size:24px;color:var(--ink);letter-spacing:4px}

/* contact */
.contact{top:3160px;height:700px}
.contact .photo{left:0;top:0;width:1200px;height:700px;background:linear-gradient(120deg,#2c2c2c 0%,#5d5d5d 40%,#8e8e8e 60%,#3a3a3a 100%)}
.contact .lead{position:absolute;left:90px;top:110px;width:420px;color:#fff;font-family:"Montserrat",sans-serif;font-size:30px;font-weight:500;line-height:1.3}
.form-card{position:absolute;left:592px;top:100px;width:520px;height:580px;background:rgba(255,255,255,.93);padding:28px 40px}
.form-card .eyebrow{display:block;text-align:center;font-size:14px}
.form-card h2{text-align:center;font-size:24px;color:var(--ink);margin-top:6px}
.form-row{display:flex;gap:30px;margin-top:30px}
.field{flex:1;font-size:11px;color:var(--muted)}
.field .box{height:40px;border:1.5px solid var(--line);background:#fff;margin-top:6px;padding:10px;font-size:11px}
.field .box.tall{height:130px}
.form-card .btn{position:absolute;left:218px;bottom:30px;border-radius:6px;font-size:12px}

/* blogs */
.blogs{top:3990px;height:610px}
.blogs .section-title{position:absolute;top:10px;width:1200px}
.post{position:absolute;top:126px;width:232px}
.post .photo{position:relative;width:232px;height:218px;background:linear-gradient(145deg,#2a2a2a,#7a7a7a 60%,#4a4a4a)}
.post .date{position:absolute;left:0;top:14px;background:#fff;color:var(--ink);font-size:11px;font-weight:600;padding:6px 12px;font-family:"Montserrat",sans-serif}
.post .more{position:absolute;left:74px;top:94px;border:1px solid #fff;color:#fff;font-size:11px;padding:6px 12px;font-family:"Montserrat",sans-serif}
.post h3{font-family:"Open Sans",sans-serif;font-weight:400;font-size:16px;color:var(--ink);line-height:1.4;margin-top:30px}
.post p{font-size:13px;color:var(--muted);line-height:1.5;margin-top:16px}

/* footer */
.site-footer{top:4600px;height:484px;background:var(--dark);color:#cfcfcf}
.footer-brand{position:absolute;left:100px;top:72px;width:110px;height:100px;border:1px solid #777;color:#fff;font-family:"Montserrat",sans-serif;font-weight:600;font-size:12px;text-align:center;padding-top:34px;line-height:1.5}
.site-footer .about-text{position:absolute;left:100px;top:200px;width:200px;font-size:12px;line-height:1.55}
.fcol{position:absolute;top:80px;font-size:12px}
.fcol h4{color:#fff;font-size:13px;font-weight:600;margin-bottom:26px;letter-spacing:.5px}
.fcol li{list-style:none;margin-bottom:18px}
.subscribe{display:flex;margin-top:2px}
.subscribe .in{width:130px;height:28px;background:#fff;color:#999;font-size:10px;padding:7px 8px}
.subscribe .go{width:32px;height:28px;background:#777;display:flex;align-items:center;justify-content:center}
.socials{display:flex;gap:12px;margin-top:14px}
.socials i{width:16px;height:16px;border-radius:50%;background:#bdbdbd;display:block}
.copyright{position:absolute;left:0;top:440px;width:1200px;height:44px;background:#2a2a2a;text-align:center;font-size:11px;line-height:44px;color:#bbb}
</style>
</head>
<body>

<section class="hero">
  <div class="photo" role="img" aria-label="Photo of a detailer power washing a car at a wash bay"></div>
  <svg class="abs" style="left:0;top:660px" width="1200" height="120" viewBox="0 0 1200 120">
    <polygon points="0,40 600,80 1200,40 1200,120 0,120" fill="#ffffff"/>
    <polyline points="0,44 600,84 1200,44" fill="none" stroke="#c9bb9c" stroke-width="4"/>
  </svg>
  <div class="hero-copy">
    <h1><span class="l1" style="display:block">WE LOVE YOUR CAR</span><span class="l2" style="display:block">THE SAME AS YOU DO</span></h1>
    <a class="btn">EXPLORE</a>
  </div>
  <svg class="hero-arrow" style="left:36px" width="24" height="44" viewBox="0 0 24 44"><polyline points="20,2 4,22 20,42" fill="none" stroke="#fff" stroke-width="3"/></svg>
  <svg class="hero-arrow" style="right:36px" width="24" height="44" viewBox="0 0 24 44"><polyline points="4,2 20,22 4,42" fill="none" stroke="#fff" stroke-width="3"/></svg>
  <div class="dots" style="left:570px;top:676px"><i class="on"></i><i></i><i></i></div>
</section>

<header class="site-header">
  <div class="brand-tab">HARBOR LINE<br>DETAILING</div>
  <nav class="nav">
    <span class="current">HOME</span><span>ABOUT</span><span>SERVICES</span><span>PAGES</span><span>BLOGS</span><span class="pill">CONTACT</span>
  </nav>
</header>

<section class="about">
  <span class="eyebrow">ABOUT US</span>
  <h2>HARBOR LINE MOBILE<br>DETAILING</h2>
  <p>Our service is not just a wash as it is a real treatment for your car. The car gets a rebirth due to our CCG which is truly regenerative therapy. Research has shown, steam pressure cleaning prevents corrosion for a period of 2 years when compared to the regular use of water for cleaning.</p>
  <a class="btn">Read More</a>
  <div class="frame"></div>
  <div class="photo" role="img" aria-label="Photo of a detailer cleaning the rear of a dark car"></div>
</section>

<section class="services">
  <div class="section-title"><span class="eyebrow">OUR SERVICES</span><h2>WE ARE A FULL SERVICES</h2></div>

  <div class="service" style="left:128px">
    <div class="icon"><svg width="50" height="40" viewBox="0 0 50 40" fill="none" stroke="#222" stroke-width="2.5"><path d="M6 26 L10 14 Q12 10 16 10 H34 Q38 10 40 14 L44 26 V32 H6 Z"/><circle cx="15" cy="32" r="4" fill="#fff"/><circle cx="35" cy="32" r="4" fill="#fff"/><path d="M18 3 v4 M25 1 v6 M32 3 v4"/></svg></div>
    <h3>CAR WASHING</h3>
    <p>Lorem ipsum door sit amet, consectetur adipiscing elit, sed do eiusmod tempor incididunt ut labore et dolore magna aliquatempor incididunt ut labore et dolore magna aliqua</p>
  </div>
  <div class="service" style="left:372px">
    <div class="icon active"><svg width="44" height="44" viewBox="0 0 44 44" fill="none" stroke="#fff" stroke-width="2.5"><path d="M22 6 C30 18 34 24 34 29 a12 12 0 0 1 -24 0 C10 24 14 18 22 6 Z"/></svg></div>
    <h3 style="color:#8a8a8a">POWER WASHING</h3>
    <p>Lorem ipsum door sit amet, consectetur adipiscing elit, sed do eiusmod tempor incididunt ut labore et dolore magna aliquatempor incididunt ut labore et dolore magna aliqua</p>
  </div>
  <div class="service" style="left:620px">
    <div class="icon"><svg width="48" height="44" viewBox="0 0 48 44" fill="none" stroke="#222" stroke-width="2.5"><path d="M4 22 L24 6 L44 22"/><path d="M10 18 V40 H38 V18"/><rect x="19" y="26" width="10" height="14"/></svg></div>
    <h3>REAIDENTIAL VISIT<br>CAR WASHING</h3>
    <p>Lorem ipsum door sit amet, consectetur adipiscing elit, sed do eiusmod tempor incididunt ut labore et dolore magna aliquatempor incididunt ut labore et dolore magna aliquat dolore</p>
  </div>
  <div class="service" style="left:860px">
    <div class="icon"><svg width="48" height="44" viewBox="0 0 48 44" fill="none" stroke="#222" stroke-width="2.5"><path d="M6 20 L24 6 L42 20 V40 H6 Z"/><path d="M16 32 h16 M18 26 h12"/></svg></div>
    <h3>RESIDENTIAL<br>CLEANING</h3>
    <p>Lorem ipsum door sit amet, consectetur adipiscing elit, sed do eiusmod tempor incididunt ut labore et dolore magna aliquatempor incididunt ut labore et dolore magna aliqua</p>
  </div>
  <a class="btn">View More</a>
</section>

<section class="why">
  <div class="photo" role="img" aria-label="Photo of a smiling cleaner in overalls holding a squeegee"></div>
  <span class="eyebrow">WHY CHOOSE US</span>
  <h2>OUR SERVICE IS NOT<br>JUST A WASH</h2>
  <p>Our service is not just a wash as it is a real treatment for your car. The car gets a rebirth due to our CCG which is truly regenerative therapy.</p>
  <ul>
    <li><svg width="10" height="12" viewBox="0 0 10 12"><polygon points="0,0 10,6 0,12" fill="#222"/></svg>EASY BOOKING</li>
    <li><svg width="10" height="12" viewBox="0 0 10 12"><polygon points="0,0 10,6 0,12" fill="#222"/></svg>PERFECT SERVICING</li>
    <li><svg width="10" height="12" viewBox="0 0 10 12"><polygon points="0,0 10,6 0,12" fill="#222"/></svg>SPEED AND SECURITY</li>
    <li><svg width="10" height="12" viewBox="0 0 10 12"><polygon points="0,0 10,6 0,12" fill="#222"/></svg>ENVIRONMENTALLY FRIENDLY</li>
  </ul>
  <a class="btn">Explore</a>
</section>

<section class="stats">
  <svg class="band" width="1200" height="340" viewBox="0 0 1200 340" role="img" aria-label="Dark grey band with water droplets texture">
    <defs><linearGradient id="statsFill" x1="0" y1="0" x2="1" y2="1"><stop offset="0" stop-color="#5a5a5a"/><stop offset=".5" stop-color="#3f3f3f"/><stop offset="1" stop-color="#555"/></linearGradient></defs>
    <polygon points="0,0 1200,0 1200,255 600,335 0,255" fill="url(#statsFill)"/>
  </svg>
  <div class="stat" style="left:213px"><div class="ring">50+</div><span>Trained<br>Staff</span></div>
  <div class="stat" style="left:425px"><div class="ring">1000</div><span>Satisfied<br>Clients</span></div>
  <div class="stat" style="left:637px"><div class="ring">23</div><span>Branches</span></div>
  <div class="stat" style="left:833px"><div class="ring">1400</div><span>Jobs Done</span></div>
</section>

<section class="testimonials">
  <div class="section-title"><span class="eyebrow">TESTIMONIALS</span><h2>WHAT OUR CLIENTS SAY</h2></div>
  <div class="rail"></div>
  <div class="arrow" style="left:462px"><svg width="12" height="18" viewBox="0 0 12 18"><polyline points="10,2 3,9 10,16" fill="none" stroke="#222" stroke-width="2"/></svg></div>
  <div class="arrow" style="left:696px"><svg width="12" height="18" viewBox="0 0 12 18"><polyline points="2,2 9,9 2,16" fill="none" stroke="#222" stroke-width="2"/></svg></div>
  <div class="avatar" role="img" aria-label="Client portrait"></div>
  <blockquote>Our service is not just a wash as it is a real treatment for your car. The car gets a rebirth due to our CCG which is truly regenerative therapy. Our service is not just a wash as it is a real treatment for your car. The car gets a rebirth due to our CCG which is truly regenerative therapy.Our service is not just a wash as</blockquote>
  <cite>DANIEL REEVE</cite>
  <div class="stars">★★★★★</div>
  <div class="dots" style="left:570px;top:445px"><i style="background:#555"></i><i></i><i></i></div>
</section>

<section class="contact">
  <div class="photo" role="img" aria-label="Photo of a white sports car being washed with spray and foam"></div>
  <svg class="abs" style="left:0;top:600px" width="1200" height="100" viewBox="0 0 1200 100"><polygon points="0,0 600,90 1200,0 1200,100 0,100" fill="#ffffff"/></svg>
  <p class="lead">For all your needs of car wash, deep cleaning</p>
  <div class="form-card">
    <span class="eyebrow">CONTACT FORM</span>
    <h2>SEND US MESSAGE</h2>
    <div class="form-row"><div class="field">Name*<div class="box"></div></div><div class="field">Phone*<div class="box"></div></div></div>
    <div class="form-row" style="margin-top:16px"><div class="field">E-mail*<div class="box"></div></div></div>
    <div class="form-row" style="margin-top:16px"><div class="field">Your Message<div class="box tall">Type Your Message Here</div></div></div>
    <a class="btn">SUBMIT</a>
  </div>
</section>

<section class="blogs">
  <div class="section-title"><span class="eyebrow">OUR BLOGS</span><h2>READ OUR LATEST BLOGS</h2></div>
  <article class="post" style="left:180px">
    <div class="photo" role="img" aria-label="Photo of a clean car dashboard interior"><span class="date">15 July<br>2020</span></div>
    <h3>Quality Assurance Cleaning interior side</h3>
    <p>Spare ribs porchetta tenderloin, landjaeger pork jerky turducken rump landjaeger pork chop filet mignon ball</p>
  </article>
  <article class="post" style="left:484px">
    <div class="photo" role="img" aria-label="Photo of a car washing service in progress"><span class="date">18 July<br>2020</span><span class="more">READ MORE</span></div>
    <h3>Residential Cleaning &amp; car washing service</h3>
    <p>Spare ribs porchetta tenderloin, landjaeger pork jerky turducken rump landjaeger pork chop filet mignon ball</p>
  </article>
  <article class="post" style="left:788px">
    <div class="photo" role="img" aria-label="Photo of a windshield being cleaned with a squeegee"><span class="date">20 June<br>2020</span></div>
    <h3>Mirror cleaning With sampoo - glass clean</h3>
    <p>Spare ribs porchetta tenderloin, landjaeger pork jerky turducken rump landjaeger pork chop filet mignon ball</p>
  </article>
</section>

<footer class="site-footer">
  <div class="footer-brand">HARBOR LINE<br>DETAILING</div>
  <p class="about-text">HLM detailing is a specialty cleaning service caring for your car, your home and your drive in every season of the year.</p>
  <div class="fcol" style="left:372px"><h4>MENUS</h4><ul><li>Home</li><li>About</li><li>Service</li><li>Blogs</li><li>Pages</li></ul></div>
  <div class="fcol" style="left:512px"><h4>USEFUL LINKS</h4><ul><li>News</li><li>Contact</li><li>Privacy Policy</li><li>Terms &amp; Conditions</li></ul></div>
  <div class="fcol" style="left:700px"><h4>CONTACT US</h4><ul><li>Phone: (333) 000 0000<br>Email: hello@harborlinedetail.com</li><li style="margin-top:22px">Address: 00000 Lorem<br>ipsum place, area, Australia</li></ul></div>
  <div class="fcol" style="left:945px"><h4>SUBSCRIBE</h4>
    <div class="subscribe"><div class="in">Enter email</div><div class="go"><svg width="12" height="12" viewBox="0 0 12 12"><polygon points="0,0 12,6 0,12 2,6" fill="#fff"/></svg></div></div>
    <h4 style="margin-top:22px;margin-bottom:0">FOLLOW US</h4>
    <div class="socials"><i></i><i></i><i></i><i></i></div>
  </div>
  <div class="copyright">© Copyright 2020, HLMdetailing All Rights Reserved</div>
</footer>

</body>
</html>
```